Business Card Design Project

for a second hand vintage clothing store. shop name is The Velvet Cupboard

Cards to be double sided

The name on the card is Joanna Whitfield

Information to put on card:

The Velvet Cupboard
Joanna Whitfield (no job title)
42/871 Dunmore St, Glenwick, Sydney, NSW, 2187.
Mobile: 0412 905 261
Email: thevelvetcupboard@mailbox.com.au
Web: www.thevelvetcupboard.com.au

Target Market(s)

Women looking at vintage clothing

Industry/Entity Type

Clothing

```html
<!DOCTYPE html>
<html lang="en">
<head>
<meta charset="utf-8">
<title>The Velvet Cupboard – Business Card</title>
<link rel="stylesheet" href="https://fonts.googleapis.com/css2?family=Arimo:wght@400&display=swap">
<style>
  :root {
    --backdrop: #e9e4df;
    --plum: #6b1a53;
    --plum-deep: #431232;
    --amber: #e27a12;
    --gold: #cdb67c;
    --pale-gold: #efe08c;
    --card-w: 852px;
    --card-h: 487px;
  }
  * { margin: 0; padding: 0; box-sizing: border-box; }
  html, body {
    width: 1163px;
    height: 1200px;
    overflow: hidden;
    background: var(--backdrop);
    font-family: "Arimo", Arial, sans-serif;
  }
  .canvas {
    position: relative;
    width: 1163px;
    height: 1200px;
  }
  .card {
    position: absolute;
    left: 157px;
    width: var(--card-w);
    height: var(--card-h);
    background: var(--plum);
    overflow: hidden;
  }
  .card--front { top: 71px; }
  .card--back { top: 643px; }
  .card__waves {
    position: absolute;
    inset: 0;
    width: 100%;
    height: 100%;
  }
  .card__waves .band { fill: var(--plum-deep); }
  .shop-name {
    position: absolute;
    white-space: nowrap;
    font-weight: 400;
    letter-spacing: 0.5px;
  }
  .shop-name--top-left {
    left: 34px;
    top: 42px;
    font-size: 36px;
    color: var(--gold);
  }
  .shop-name--bottom-right {
    right: 32px;
    top: 372px;
    font-size: 36px;
    color: var(--gold);
  }
  .shop-name--centre {
    left: 0;
    right: 0;
    top: 238px;
    text-align: center;
    font-size: 46px;
    color: var(--pale-gold);
  }
  .holder-name {
    position: absolute;
    left: 0;
    right: 0;
    top: 232px;
    text-align: center;
    font-size: 38px;
    font-weight: 400;
    color: var(--amber);
    word-spacing: 10px;
  }
  .identity {
    position: absolute;
    left: 49px;
    top: 47px;
    color: var(--amber);
    font-size: 20px;
    line-height: 41px;
    word-spacing: 6px;
  }
  .contact {
    position: absolute;
    left: 416px;
    top: 352px;
    list-style: none;
    color: var(--amber);
    font-size: 15px;
    line-height: 29px;
    letter-spacing: 0.3px;
    word-spacing: 3px;
    white-space: nowrap;
  }
</style>
</head>
<body>
<main class="canvas">

  <section class="card card--front" aria-label="Business card front">
    <svg class="card__waves" viewBox="0 0 1050 600" preserveAspectRatio="none" aria-hidden="true">
      <path class="band" d="M0,265 C150,205 340,180 480,180 C700,184 990,205 1050,100 L1050,337 C950,410 700,420 480,412 C250,405 60,420 0,500 Z"/>
    </svg>
    <p class="shop-name shop-name--top-left">The Velvet Cupboard</p>
    <h1 class="holder-name">Joanna Whitfield</h1>
    <p class="shop-name shop-name--bottom-right">The Velvet Cupboard</p>
  </section>

  <section class="card card--back" aria-label="Business card back">
    <svg class="card__waves" viewBox="0 0 1050 600" preserveAspectRatio="none" aria-hidden="true">
      <path class="band" d="M0,265 C150,205 340,180 480,180 C700,184 990,205 1050,100 L1050,337 C950,410 700,420 480,412 C250,405 60,420 0,500 Z"/>
    </svg>
    <div class="identity">
      <p>The Velvet Cupboard</p>
      <p>Joanna Whitfield （no job title）</p>
    </div>
    <p class="shop-name shop-name--centre">The Velvet Cupboard</p>
    <ul class="contact">
      <li>Mobile: 0412 905 261</li>
      <li>Email: thevelvetcupboard@mailbox.com.au</li>
      <li>Web: www.thevelvetcupboard.com.au</li>
      <li>42/871 Dunmore St, Glenwick, Sydney, NSW, 2187</li>
    </ul>
  </section>

</main>
</body>
</html>
```